Redesign two existing website pages and one new landing page for dental office

I need to redesign two webpages on my dental website, the Home page (http://brelvoortdental.com) and the Dental Implant Services page (http://www.brelvoortdental.com/dental-implant-services) and also create a landing page for the Dental Implant Services page.

Please use the same color scheme, slogans and subtitles for the redesign pages and create a reserved video spot on each page. The video spots should not be too big but not too small either and positioned in a central key location on each of the pages. The final redesigned pages should communicate leadership, confidence and trust.

The new landing page for the Dental implant Services page must not have any hyperlinks on the page and must entice the viewer to give name and email before downloading a "Free" eBook called "Is a Fresh Smile Worth Waiting For?" Any added photo images to this new page must be smiling.
Updates

Project Deadline Extended Reason: I got feedback that my project was not long enough so I'm extending it by 5 days. Added Thursday, April 16, 2015

Target Market(s)

People who are middle-age to seniors.

Industry/Entity Type

Dental

Coding

Coded - Design and coding required

Number of Pages Required

3 page

Requirements
Must have
• Compatible with existing website colors and theme.

```html
<!DOCTYPE html>
<html lang="en">
<head>
<meta charset="utf-8">
<title>Brelvoort Dental Care — Family Dental Care in Sugar Land</title>
<link href="https://fonts.googleapis.com/css2?family=Raleway:wght@400;500;600;700&display=swap" rel="stylesheet">
<style>
:root{
  --forest:#3d5e55;
  --forest-dark:#2f4b43;
  --sage:#7a9e94;
  --sage-band:#85a8a0;
  --cream:#eeeee0;
  --ink:#2d3f3a;
  --muted:#777;
  --footer:#262626;
  --footer-deep:#121212;
  --white:#fff;
}
*{box-sizing:border-box;margin:0;padding:0}
html,body{width:915px;height:1200px;overflow:hidden}
body{font-family:'Raleway',sans-serif;color:var(--ink);background:var(--white);position:relative}
a{color:inherit;text-decoration:none}
ul{list-style:none}

.top-nav{position:absolute;left:0;top:0;width:915px;height:40px;background:var(--forest);display:flex;align-items:center}
.top-nav .links{display:flex;margin-left:66px;height:40px}
.top-nav .links a{color:#e3ece8;font-size:10px;letter-spacing:.5px;display:flex;align-items:center;padding:0 26px}
.top-nav .links a.active{background:var(--forest-dark);color:#a6cbbf;padding:0 29px}
.social{position:absolute;right:66px;display:flex;gap:5px}
.social span{width:16px;height:16px;border-radius:50%;background:#6b7f79}
.social span.on{background:#2aa0d8}

.header{position:absolute;top:40px;left:0;width:915px;height:67px}
.brand{position:absolute;left:66px;top:20px;font-size:24px;font-weight:500;color:var(--sage);display:flex;align-items:center;gap:8px}
.brand i{width:10px;height:10px;border-radius:50%;background:var(--forest);display:block}
.quick{position:absolute;top:20px;display:flex;align-items:center;gap:6px;font-size:10px;color:var(--sage);line-height:1.2}
.quick svg{width:20px;height:30px}
.quick.call{color:#222;font-weight:600}
.quick.call small{display:block;font-weight:500;font-size:10px}

.hero{position:absolute;top:107px;left:0;width:915px;height:308px;background:linear-gradient(180deg,#8fae7a 0%,#c9cfa8 45%,#d9b6a2 100%)}

.intro{position:absolute;top:415px;left:0;width:915px;height:110px}
.intro .kicker{position:absolute;left:66px;top:18px;font-size:23px;letter-spacing:3px;color:#444}
.intro h1{position:absolute;left:64px;top:40px;font-size:38px;font-weight:700;color:var(--sage);letter-spacing:.3px}
.intro h1 span{font-size:17px;font-weight:400;color:#888;letter-spacing:0}
.intro p{position:absolute;left:66px;top:82px;font-size:10px;color:#888}
.btn{position:absolute;height:28px;border:1px solid var(--forest);border-radius:15px;display:flex;align-items:center;justify-content:center;font-size:10px;font-weight:500;color:#222}
.btn.light{color:var(--sage);border-color:var(--sage)}

.services{position:absolute;top:525px;left:0;width:915px;height:160px;background:var(--cream)}
.service{position:absolute;top:30px;width:190px}
.service h2{font-size:17px;font-weight:600;line-height:1.2;color:var(--forest);margin-bottom:10px}
.service li,.posts li{font-size:10px;color:#888;padding-left:14px;position:relative;line-height:1.4}
.service li::before,.posts li::before{content:"";position:absolute;left:0;top:3px;width:5px;height:5px;border:1px solid #666;border-radius:50%}

.band{position:absolute;top:685px;left:0;width:915px;height:47px;background:var(--sage-band)}
.band p{position:absolute;left:67px;top:17px;font-size:11.5px;font-weight:600;color:var(--white)}
.band .btn{border-color:var(--white);color:var(--white);right:66px;top:10px;width:174px}

.video-col{position:absolute;left:66px;top:768px}
.video-col h3{font-size:17px;font-weight:600}
.video-col p{font-size:10px;color:#888;margin-top:6px}
.video{position:absolute;left:66px;top:812px;width:370px;height:192px;background:linear-gradient(135deg,#3a3a3a,#1c1c1c)}
.play{position:absolute;left:157px;top:68px;width:56px;height:56px;border-radius:50%;background:var(--sage)}
.play::after{content:"";position:absolute;left:22px;top:17px;border-left:16px solid var(--white);border-top:11px solid transparent;border-bottom:11px solid transparent}

.posts{position:absolute;left:458px;top:768px;width:190px}
.posts h3{font-size:17px;font-weight:600;color:var(--sage);line-height:1.2;margin-bottom:10px}
.posts li{margin-bottom:10px;line-height:1.2}
.posts .all{font-size:10px;font-weight:600;color:#666;padding-left:13px}

.promo{position:absolute;left:654px;width:200px}
.promo h3{font-size:17px;font-weight:600;line-height:1.2}
.promo p{font-size:10px;margin-top:8px;color:#333}
.promo .pill{margin-top:10px;width:112px;height:27px;border-radius:14px;display:flex;align-items:center;justify-content:center;font-size:10px;font-weight:500}
.pill.solid{background:var(--forest);color:var(--white)}
.pill.outline{border:1px solid var(--forest);color:var(--forest)}

.footer{position:absolute;top:1033px;left:0;width:915px;height:115px;background:var(--footer);color:#bbb;font-size:10px}
.footer .brand{color:var(--white);top:32px;font-size:22px}
.footer .copy{position:absolute;left:70px;top:76px}
.footer .addr{position:absolute;left:353px;top:46px;line-height:1.8}
.footer .contact{position:absolute;right:66px;top:46px;text-align:right;line-height:1.8}
.footer .contact b{color:var(--white);font-weight:600}
.bottom-nav{position:absolute;top:1148px;left:0;width:915px;height:52px;background:var(--footer-deep);display:flex;align-items:center}
.bottom-nav .links{display:flex;gap:37px;margin-left:66px}
.bottom-nav .links a{color:#ccc;font-size:10px}
.bottom-nav .links a.active{color:var(--sage)}
</style>
</head>
<body>

<nav class="top-nav">
  <div class="links">
    <a class="active" href="#">HOME</a><a href="#">ABOUT US</a><a href="#">DENTAL SERVICES</a><a href="#">BLOG</a><a href="#">CONTACT US</a><a href="#">TESTIMONIALS</a>
  </div>
  <div class="social"><span></span><span></span><span class="on"></span><span></span><span></span></div>
</nav>

<header class="header">
  <div class="brand"><i></i>Brelvoort Dental Care</div>
  <div class="quick" style="left:401px">
    <svg viewBox="0 0 20 30"><rect x="2" y="1" width="16" height="28" rx="2" fill="none" stroke="#7a9e94"/></svg>Get Dr. Brelvoort's<br>Mobile App</div>
  <div class="quick" style="left:522px">
    <svg viewBox="0 0 20 30"><rect x="2" y="1" width="16" height="28" rx="2" fill="none" stroke="#7a9e94"/><path d="M6 8h8M6 12h8M6 16h8" stroke="#7a9e94"/></svg>Request an<br>Appointment</div>
  <div class="quick" style="left:637px">
    <svg viewBox="0 0 20 30"><rect x="1" y="4" width="15" height="24" fill="none" stroke="#7a9e94"/><path d="M8 20L19 4" stroke="#7a9e94"/></svg>New Patient<br>Online Forms</div>
  <div class="quick call" style="left:757px">
    <svg viewBox="0 0 20 30"><rect x="2" y="1" width="16" height="28" rx="2" fill="none" stroke="#222"/><circle cx="10" cy="25" r="1.5" fill="#222"/></svg><div>Call Us Today!<small>(281) 555-0147</small></div></div>
</header>

<div class="hero" role="img" aria-label="Photo of a smiling multi-generation family outdoors among trees"></div>

<section class="intro">
  <div class="kicker">LIFE-CHANGING</div>
  <h1>FAMILY DENTAL CARE <span>IN SUGAR LAND</span></h1>
  <p>Ut wisi enim ad minim veniam, quis nostrud exerci tation ullamcorper suscipit lobortis nisl ut aliquip ex ea commodo consequat.</p>
  <a class="btn" href="#" style="left:675px;top:22px;width:174px">REQUEST AN APPOINTMENT</a>
  <a class="btn light" href="#" style="left:675px;top:63px;width:174px">CONTACT US</a>
</section>

<section class="services">
  <div class="service" style="left:66px"><h2>Beautiful<br>Dentures</h2>
    <ul><li>What is a Denture?</li><li>Who Needs a Denture?</li><li>Just How Are Dentures Made?</li></ul></div>
  <div class="service" style="left:262px"><h2>Cosmetic<br>Dentistry</h2>
    <ul><li>Whiten Your Teeth</li><li>Porcelain Veneers</li><li>Clear Aligner Therapy Orthodontics</li></ul></div>
  <div class="service" style="left:458px"><h2>Dental Implant<br>Services</h2>
    <ul><li>Anchorage to the jaw bone</li><li>Replaces 1 or more missing teeth</li><li>Stabilizes loose, floppy dentures</li></ul></div>
  <div class="service" style="left:654px"><h2>Sedation<br>Dentistry</h2>
    <ul><li>Control Dental Fear with Sedation Dentistry</li><li>Dental Pain Management</li><li>Relaxed and Tranquil Treatment</li></ul></div>
</section>

<section class="band">
  <p>COMPREHENSIVE FAMILY DENTISTRY IN ONE SUGAR LAND DENTAL OFFICE!</p>
  <a class="btn" href="#">REQUEST AN APPOINTMENT</a>
</section>

<div class="video-col"><h3>Don’t Wait ’til it Hurts!</h3><p>Get acquanted today with comfortable dental care.</p></div>
<div class="video" role="img" aria-label="Video thumbnail reading Quick Tips"><div class="play"></div></div>

<div class="posts">
  <h3>Recent Blog<br>Posts</h3>
  <ul>
    <li>Conscious Sedation: A Way to Deal with Anxiety at the Dentist's Office</li>
    <li>Pediatric Dentists and Their Importance in Today's World</li>
    <li>Tooth Implant Facts</li>
    <li>Is Sedation Dentistry Cost Affordable?</li>
    <li>How to Prepare for Oral Surgery</li>
    <li>Tooth Implant Facts</li>
  </ul>
  <div class="all">SEE ALL &gt;&gt;</div>
</div>

<div class="promo" style="top:768px"><h3>Dental Emergency<br>Services</h3><p>Stop Pain From Tooth Trauma and Infection</p><a class="pill solid" href="#">LEARN MORE</a></div>
<div class="promo" style="top:889px"><h3>Dental Hygiene<br>Services</h3><p>Achieve Better Health With Prevention</p><a class="pill outline" href="#">LEARN MORE</a></div>

<footer class="footer">
  <div class="brand"><i style="background:#fff"></i>Brelvoort Dental Care</div>
  <div class="copy">©2015 Brelvoort Dental Care.</div>
  <div class="addr">Larkspur Medical Center, 2480 Orchard Pkwy,<br>Ste. #310, Sugar Land, TX 77479</div>
  <div class="contact">Email Us &nbsp;&nbsp;&nbsp;&nbsp;&nbsp; <b>Phone &nbsp;(281) 555-0147</b><br>Directions to the Larkspur Medical Center &gt;&gt;</div>
</footer>
<nav class="bottom-nav">
  <div class="links"><a class="active" href="#">HOME</a><a href="#">ABOUT US</a><a href="#">DENTAL SERVICES</a><a href="#">BLOG</a><a href="#">CONTACT US</a><a href="#">TESTIMONIALS</a></div>
  <div class="social"><span></span><span></span><span class="on"></span><span></span><span></span></div>
</nav>

</body>
</html>
```